Brightpath Wellness Partners

Please design a business card that is colorful but at the same time easy to read. We are based out on Miami Florida. We are a small start up healthcare company that has been in operation for 1 year. Our clients are Hospitals, Insurance companies, and Manage Care health companies. We are growing quickly and lead the niche we are in. Please make the card 2 sided on the front will be the typical info. Logo, Company Name, Persons Name, Title, Cell #, Office #, Fax#, email, website. No address. On the back we will list 5 services that we do. For example Care Transitions, Case management, Risk assessment, Utilization Review.
Target Market(s)
CEO's and COO's of hospitals and healthcare companies.
Industry/Entity Type
Healthcare

```html
<!DOCTYPE html>
<html lang="en">
<head>
<meta charset="utf-8">
<title>Brightpath Wellness Partners – Business Card</title>
<link rel="stylesheet" href="https://fonts.googleapis.com/css2?family=Lato:ital,wght@0,400;0,700;0,900;1,700&display=swap">
<style>
  :root {
    --backdrop: #e4e5e7;
    --card: #fbfbfa;
    --ink: #1c1c1c;
    --ink-soft: #3d3d3d;
    --brand-green: #1aa64a;
    --brand-blue: #1f5fae;
    --brand-navy: #2b2f8f;
    --rule: #8a8a8a;
  }
  * { box-sizing: border-box; margin: 0; padding: 0; }
  html, body {
    width: 1200px; height: 926px; overflow: hidden;
    background: var(--backdrop);
    font-family: "Lato", Arial, sans-serif;
    color: var(--ink);
  }
  .sheet {
    width: 1200px; height: 926px;
    display: flex; flex-direction: column; align-items: center; justify-content: center;
    gap: 40px;
  }
  .card {
    position: relative;
    width: 700px; height: 400px;
    background: var(--card);
    box-shadow: 0 4px 14px rgba(0,0,0,.18);
  }

  /* Front */
  .front__company {
    position: absolute; left: 48px; top: 42px;
    font-size: 33px; font-weight: 400; color: var(--ink);
  }
  .front__person {
    position: absolute; left: 58px; top: 128px;
    font-size: 31px; color: var(--brand-green); font-weight: 400;
  }
  .front__person strong { font-weight: 700; }
  .front__title {
    font-size: 16px; font-weight: 700; color: var(--ink); letter-spacing: .5px;
  }
  .contact {
    position: absolute; left: 58px; top: 186px;
    list-style: none; font-size: 17px; line-height: 27px;
  }
  .contact__label { color: var(--brand-blue); font-weight: 700; font-style: italic; }
  .contact__value { color: var(--ink); }
  .front__mark {
    position: absolute; right: 48px; bottom: 52px;
    display: flex; align-items: center; gap: 12px;
  }
  .brand-dot {
    width: 34px; height: 34px; border-radius: 50%;
    background: var(--brand-green); flex: none;
  }
  .brand-name {
    font-size: 20px; font-weight: 900; line-height: 1.1; color: var(--brand-navy);
  }

  /* Back */
  .back__mark {
    position: absolute; left: 0; right: 0; top: 62px;
    display: flex; align-items: center; justify-content: center; gap: 18px;
  }
  .back__mark .brand-dot { width: 56px; height: 56px; }
  .back__mark .brand-name { font-size: 34px; color: var(--ink-soft); }
  .back__rule {
    position: absolute; left: 0; right: 0; height: 1px; background: var(--rule);
  }
  .back__rule--top { top: 210px; }
  .back__rule--bottom { top: 330px; }
  .services {
    position: absolute; left: 0; right: 0; top: 230px;
    text-align: center; text-transform: uppercase;
    font-size: 19px; letter-spacing: 1px; line-height: 34px; color: var(--ink);
  }
</style>
</head>
<body>
<main class="sheet">
  <section class="card card--front" aria-label="Card front">
    <h1 class="front__company">Brightpath Wellness Partners</h1>
    <p class="front__person">Marcus <strong>Delgado</strong> <span class="front__title">-TITLE</span></p>
    <ul class="contact">
      <li><span class="contact__label">cell:</span> <span class="contact__value">305-555-0142</span></li>
      <li><span class="contact__label">office:</span> <span class="contact__value">305-555-0187</span></li>
      <li><span class="contact__label">fax:</span> <span class="contact__value">305-555-0193</span></li>
      <li><span class="contact__label">email:</span> <span class="contact__value">brightpathwellness.com</span></li>
      <li><span class="contact__label">web:</span> <span class="contact__value">m.delgado@brightpathwellness.com</span></li>
    </ul>
    <div class="front__mark">
      <span class="brand-dot"></span>
      <span class="brand-name">Brightpath<br>Wellness Partners</span>
    </div>
  </section>

  <section class="card card--back" aria-label="Card back">
    <div class="back__mark">
      <span class="brand-dot"></span>
      <span class="brand-name">Brightpath<br>Wellness Partners</span>
    </div>
    <div class="back__rule back__rule--top"></div>
    <p class="services">Care transitions, case management,<br>risk assessment, utilization review and manage care</p>
    <div class="back__rule back__rule--bottom"></div>
  </section>
</main>
</body>
</html>
```